PRVD Traditional Business Card Project

Please see attached....just a simple business card... on attachment- please use the exact font, style, etc as the attached "Pat Everard Wynne" card... however, replace with the "Owen Reginald Talbot" text and address below the card.

```html
<!DOCTYPE html>
<html lang="en">
<head>
<meta charset="utf-8">
<title>PRVD Business Card</title>
<link rel="stylesheet" href="https://fonts.googleapis.com/css2?family=Tinos:wght@400&display=swap">
<style>
  :root {
    --page-bg: #151617;
    --card-bg: #1f2123;
    --ink: #d9d9d9;
    --ink-soft: #bcbcbc;
    --rule: #c9c9c9;
  }
  * { margin: 0; padding: 0; box-sizing: border-box; }
  html, body {
    width: 1200px; height: 800px; overflow: hidden;
    background: var(--page-bg);
  }
  .card {
    position: absolute; left: 150px; top: 143px;
    width: 900px; height: 514px;
    background: var(--card-bg);
    font-family: "Tinos", "Times New Roman", serif;
    font-variant: small-caps;
    color: var(--ink);
    box-shadow: 0 18px 40px rgba(0,0,0,.45);
  }
  .card-frame { position: absolute; inset: 0; }
  .firm {
    position: absolute; left: 62px; top: 58px;
    line-height: 1.05;
  }
  .firm-name { font-size: 24px; letter-spacing: .04em; }
  .firm-sub { font-size: 15px; letter-spacing: .06em; padding-left: 40px; color: var(--ink-soft); }
  .contact {
    position: absolute; right: 62px; top: 58px;
    font-size: 17px; line-height: 1.2; letter-spacing: .03em;
  }
  .contact .email { padding-left: 28px; }
  .attorney {
    position: absolute; left: 0; right: 0; top: 205px;
    text-align: center;
  }
  .attorney-name { font-size: 50px; letter-spacing: .05em; line-height: 1; padding-left: 60px; }
  .attorney-title {
    font-size: 17px; letter-spacing: .06em; color: var(--ink-soft);
    text-align: right; padding-right: 178px; margin-top: 6px;
  }
  .address {
    position: absolute; left: 62px; bottom: 58px;
    font-size: 19px; line-height: 1.18; letter-spacing: .03em;
  }
</style>
</head>
<body>
  <article class="card">
    <svg class="card-frame" viewBox="0 0 900 514" width="900" height="514" aria-hidden="true">
      <path d="M52 22 H848 A30 30 0 0 0 878 52 V462 A30 30 0 0 0 848 492 H52 A30 30 0 0 0 22 462 V52 A30 30 0 0 0 52 22 Z"
            fill="none" stroke="var(--rule)" stroke-width="1.6"/>
      <path d="M68 30 H832 A38 38 0 0 0 870 68 V446 A38 38 0 0 0 832 484 H68 A38 38 0 0 0 30 446 V68 A38 38 0 0 0 68 30 Z"
            fill="none" stroke="var(--rule)" stroke-width="1.2"/>
    </svg>

    <div class="firm">
      <div class="firm-name">Pacific Ridge Valley</div>
      <div class="firm-sub">Defenders, PLC</div>
    </div>

    <div class="contact">
      <div>Tel (555) 210-3380</div>
      <div>Fax (555) 210-3391</div>
      <div class="email">otalbot@lawprvd.com</div>
    </div>

    <div class="attorney">
      <div class="attorney-name">Owen Reginald Talbot</div>
      <div class="attorney-title">Attorney at Law</div>
    </div>

    <div class="address">
      <div>2740 Cedar Lane, Suite B</div>
      <div>Alder Springs, CA 90412</div>
      <div>www.lawprvd.com</div>
    </div>
  </article>
</body>
</html>
```